Business Card Design - PathwayMinds

Looking for creative, modern design, two sided for PathwayMinds that is consistent with color and feel of website www.pathwayminds.example.
Updates

Back of card will be used to promote products or have a quote revolving around decisions, change, leadership, innovation, creativity. Back should also have space to promote website, but optional to use the icon. Front of the card will need to use the icon and have standard place for name, job title, phone and email. We are not looking to put a mailing address or fax. Also want space to place a few words/phrase explaining what we do...such as individual growth and organizational development or tools, training, information...in addition, want the chatterbook icon small on the front somewhere as we are also on chatterbook.

Vector file uploaded of icon.

Target Market(s)

Professional coaching for individual growth and organizational development

Industry/Entity Type

Business

Requirements
Must have
• Icon...see attached.

```html
<!DOCTYPE html>
<html lang="en">
<head>
<meta charset="utf-8">
<title>PathwayMinds — Business Card</title>
<link rel="stylesheet" href="https://fonts.googleapis.com/css2?family=Cinzel:wght@400;600&family=Junge&display=swap">
<style>
  :root {
    --page: #ece8e1;
    --card-dark: #0b0b0c;
    --card-light: #ffffff;
    --blue: #5aa3f0;
    --blue-bar: #7fb3ec;
    --blue-pale: #cfe3fb;
    --blue-deep: #1f5fd1;
    --ink: #141414;
    --white: #ffffff;
    --charcoal: #2a2d31;
  }
  * { box-sizing: border-box; margin: 0; padding: 0; }
  html, body { width: 922px; height: 1200px; overflow: hidden; background: var(--page); }
  .canvas { position: relative; width: 922px; height: 1200px; }

  .card { position: absolute; border-radius: 9px; overflow: hidden; }
  .card svg.backdrop { position: absolute; inset: 0; }

  /* Front */
  .card-front { left: 136px; top: 59px; width: 751px; height: 488px; background: var(--card-dark); }
  .brand-bar {
    position: absolute; left: 0; top: 226px; width: 340px; height: 35px;
    background: var(--blue-bar); border-radius: 0 8px 8px 0;
    font: 30px/35px "Cinzel", serif; color: var(--white); padding-left: 22px; letter-spacing: 0.5px;
  }
  .person { position: absolute; left: 21px; top: 277px; font: 23px/30px "Junge", serif; color: var(--white); }
  .contact-icon { position: absolute; width: 42px; height: 42px; }
  .contact-phone { left: 17px; top: 348px; }
  .contact-mail { left: 20px; top: 401px; }
  .emblem { position: absolute; left: 497px; top: 88px; width: 210px; height: 210px; }
  .tagline { position: absolute; left: 456px; top: 340px; width: 270px; font: 15.5px/28px "Junge", serif; color: var(--white); }
  .social { position: absolute; left: 434px; top: 430px; display: flex; align-items: center; gap: 8px; }
  .social-mark { width: 15px; height: 15px; background: var(--blue); }
  .social-link {
    background: var(--blue); color: var(--white); border-radius: 10px;
    font: 11.5px/19px "Junge", serif; padding: 0 14px; width: 256px;
  }

  /* Back */
  .card-back { left: 97px; top: 600px; width: 785px; height: 528px; background: var(--card-light); }
  .back-title {
    position: absolute; left: 0; right: 0; top: 128px; text-align: center;
    font: 600 33px/40px "Cinzel", serif; color: var(--ink); letter-spacing: 0.5px;
  }
  .title-rule { position: absolute; left: 266px; top: 172px; width: 279px; height: 2px; background: var(--blue); }
  .quotes { position: absolute; left: 8px; top: 183px; list-style: none; }
  .quotes li { display: flex; align-items: center; height: 19.2px; font: 14.2px/19px "Junge", serif; color: var(--ink); }
  .quotes svg { width: 46px; height: 10px; margin-right: 4px; flex: none; }
  .footer-band { position: absolute; left: 0; bottom: 0; width: 785px; height: 26px; }
  .footer-url { position: absolute; left: 0; right: 0; bottom: 3px; text-align: center; font: 15px/20px "Junge", serif; color: var(--white); }
  .figure-slot { position: absolute; left: 640px; top: 398px; width: 128px; height: 128px; border-radius: 50%; background: var(--charcoal); }
</style>
</head>
<body>
<main class="canvas">

  <section class="card card-front" aria-label="Card front">
    <svg class="backdrop" width="751" height="488" viewBox="0 0 751 488" aria-hidden="true">
      <path d="M0 0 H263 C180 40 80 90 0 138 Z" fill="var(--blue)"/>
      <path d="M297 94 C430 22 600 -4 690 0 H751 V138 C700 60 560 50 297 94 Z" fill="var(--blue)"/>
    </svg>

    <div class="brand-bar">PathwayMinds</div>
    <div class="person">Name-<br>Job Title-</div>

    <svg class="contact-icon contact-phone" viewBox="0 0 42 42" aria-label="Phone">
      <circle cx="21" cy="21" r="19" fill="var(--blue-deep)" stroke="var(--white)" stroke-width="2"/>
      <path d="M14 12 l5 -1 l2 6 l-3 2 c1 3 3 5 6 6 l2 -3 l6 2 l-1 5 c-10 0 -17 -7 -17 -17 z" fill="var(--white)"/>
    </svg>
    <svg class="contact-icon contact-mail" viewBox="0 0 42 42" aria-label="Email">
      <circle cx="21" cy="21" r="19" fill="var(--blue-deep)" stroke="var(--white)" stroke-width="2"/>
      <rect x="11" y="14" width="20" height="14" rx="1" fill="var(--white)"/>
      <path d="M11 14 L21 22 L31 14" fill="none" stroke="var(--blue-deep)" stroke-width="1.6"/>
    </svg>

    <svg class="emblem" viewBox="0 0 210 210" aria-label="PathwayMinds">
      <circle cx="105" cy="105" r="100" fill="var(--blue-bar)"/>
      <text x="105" y="112" text-anchor="middle" font-family="Junge, serif" font-size="22" fill="var(--white)">PathwayMinds</text>
    </svg>

    <p class="tagline">Providing tools,training,information and collaboration to achieve the results you want.</p>
    <div class="social">
      <span class="social-mark"></span>
      <span class="social-link">www.chatterbook.example/pathwayminds</span>
    </div>
  </section>

  <section class="card card-back" aria-label="Card back">
    <svg class="backdrop" width="785" height="528" viewBox="0 0 785 528" aria-hidden="true">
      <path d="M0 88 C150 36 350 38 453 127 C330 88 150 118 0 232 Z" fill="var(--blue-pale)"/>
      <path d="M512 0 C540 92 650 150 785 150 V0 Z" fill="var(--blue-pale)"/>
    </svg>

    <h1 class="back-title">PATHWAYMINDS</h1>
    <div class="title-rule"></div>

    <ul class="quotes">
      <li><svg viewBox="0 0 46 10" aria-hidden="true"><path d="M0 2 L8 5 L0 8 M8 2 L16 5 L8 8 M16 5 H38 M36 1 L46 5 L36 9 Z" fill="var(--ink)" stroke="var(--ink)" stroke-width="1.6"/></svg>"Try not to become a man of success, but rather a man of value."</li>
      <li><svg viewBox="0 0 46 10" aria-hidden="true"><path d="M0 2 L8 5 L0 8 M8 2 L16 5 L8 8 M16 5 H38 M36 1 L46 5 L36 9 Z" fill="var(--ink)" stroke="var(--ink)" stroke-width="1.6"/></svg>"We are what we repeatedly do. Excellence is not an act, it is a habit."</li>
      <li><svg viewBox="0 0 46 10" aria-hidden="true"><path d="M0 2 L8 5 L0 8 M8 2 L16 5 L8 8 M16 5 H38 M36 1 L46 5 L36 9 Z" fill="var(--ink)" stroke="var(--ink)" stroke-width="1.6"/></svg>"Life is not fair - get used to it."</li>
      <li><svg viewBox="0 0 46 10" aria-hidden="true"><path d="M0 2 L8 5 L0 8 M8 2 L16 5 L8 8 M16 5 H38 M36 1 L46 5 L36 9 Z" fill="var(--ink)" stroke="var(--ink)" stroke-width="1.6"/></svg>"The only constant is change."</li>
      <li><svg viewBox="0 0 46 10" aria-hidden="true"><path d="M0 2 L8 5 L0 8 M8 2 L16 5 L8 8 M16 5 H38 M36 1 L46 5 L36 9 Z" fill="var(--ink)" stroke="var(--ink)" stroke-width="1.6"/></svg>"Simplicity is the ultimate sophistication."</li>
      <li><svg viewBox="0 0 46 10" aria-hidden="true"><path d="M0 2 L8 5 L0 8 M8 2 L16 5 L8 8 M16 5 H38 M36 1 L46 5 L36 9 Z" fill="var(--ink)" stroke="var(--ink)" stroke-width="1.6"/></svg>"Every man I meet is my superior in some way."</li>
      <li><svg viewBox="0 0 46 10" aria-hidden="true"><path d="M0 2 L8 5 L0 8 M8 2 L16 5 L8 8 M16 5 H38 M36 1 L46 5 L36 9 Z" fill="var(--ink)" stroke="var(--ink)" stroke-width="1.6"/></svg>"The essential part of creativity is not being afraid to fail."</li>
      <li><svg viewBox="0 0 46 10" aria-hidden="true"><path d="M0 2 L8 5 L0 8 M8 2 L16 5 L8 8 M16 5 H38 M36 1 L46 5 L36 9 Z" fill="var(--ink)" stroke="var(--ink)" stroke-width="1.6"/></svg>"Music gives a soul to the universe, wings to the mind, flight to the imagination and life to everything."</li>
      <li><svg viewBox="0 0 46 10" aria-hidden="true"><path d="M0 2 L8 5 L0 8 M8 2 L16 5 L8 8 M16 5 H38 M36 1 L46 5 L36 9 Z" fill="var(--ink)" stroke="var(--ink)" stroke-width="1.6"/></svg>&nbsp;“I'll make the right decision, whichever one it is. I haveto be 100 percent, not 95 or 99.”</li>
      <li><svg viewBox="0 0 46 10" aria-hidden="true"><path d="M0 2 L8 5 L0 8 M8 2 L16 5 L8 8 M16 5 H38 M36 1 L46 5 L36 9 Z" fill="var(--ink)" stroke="var(--ink)" stroke-width="1.6"/></svg>"The height of cultivation runs to simplicity."</li>
      <li><svg viewBox="0 0 46 10" aria-hidden="true"><path d="M0 2 L8 5 L0 8 M8 2 L16 5 L8 8 M16 5 H38 M36 1 L46 5 L36 9 Z" fill="var(--ink)" stroke="var(--ink)" stroke-width="1.6"/></svg>"When you are finished changing, you're finished."</li>
      <li><svg viewBox="0 0 46 10" aria-hidden="true"><path d="M0 2 L8 5 L0 8 M8 2 L16 5 L8 8 M16 5 H38 M36 1 L46 5 L36 9 Z" fill="var(--ink)" stroke="var(--ink)" stroke-width="1.6"/></svg>"You learn when you listen. You earn whenyou listen—not just money, but respect.”</li>
      <li><svg viewBox="0 0 46 10" aria-hidden="true"><path d="M0 2 L8 5 L0 8 M8 2 L16 5 L8 8 M16 5 H38 M36 1 L46 5 L36 9 Z" fill="var(--ink)" stroke="var(--ink)" stroke-width="1.6"/></svg>"Seek first to understand, then to be understood."</li>
      <li><svg viewBox="0 0 46 10" aria-hidden="true"><path d="M0 2 L8 5 L0 8 M8 2 L16 5 L8 8 M16 5 H38 M36 1 L46 5 L36 9 Z" fill="var(--ink)" stroke="var(--ink)" stroke-width="1.6"/></svg>"The height of cultivation runs to simplicity."</li>
    </ul>

    <div class="figure-slot" role="img" aria-label="Dark silhouette illustration of a thinking figure"></div>

    <svg class="footer-band" viewBox="0 0 785 26" aria-hidden="true">
      <path d="M0 26 C4 10 14 2 40 2 H785 V26 Z" fill="var(--card-dark)"/>
    </svg>
    <p class="footer-url">www.pathwayminds.example.</p>
  </section>

</main>
</body>
</html>
```